Venture Keeper's LanternBook

We need a cover design for a printed paperback book 8.5 inches by 11 inches. The book is a self-driven business planning process for people who wish to start or buy a business, be their own boss, entrepreneurs, small and home-based business owners. We hope for a design that is fun, with a treasure map flavor.

```html
<!DOCTYPE html>
<html lang="en">
<head>
<meta charset="utf-8">
<title>Venture Keeper's LanternBook – Cover</title>
<link href="https://fonts.googleapis.com/css2?family=Londrina+Solid:wght@400;900&family=Cabin+Sketch:wght@400;700&family=Tinos&display=swap" rel="stylesheet">
<style>
  :root {
    --board: #38383a;
    --chalk: #f2f2f2;
    --chalk-dim: #d9d9d9;
    --yellow: #f0e41e;
    --mint: #86b893;
    --sketch: #6b6b6e;
    --paper: #ffffff;
  }
  * { margin: 0; padding: 0; box-sizing: border-box; }
  html, body { width: 1200px; height: 727px; overflow: hidden; background: var(--board); }
  .cover { position: relative; width: 1200px; height: 727px; background: var(--board); color: var(--chalk); }
  .abs { position: absolute; }

  .title { font-family: "Londrina Solid", sans-serif; font-weight: 900; text-align: center; line-height: 0.95; color: var(--chalk); text-transform: uppercase; }
  .title .accent { color: var(--yellow); }

  .sketch-art { position: absolute; background: radial-gradient(circle, #59595c 0%, var(--board) 75%); border-radius: 40%; }

  /* back cover */
  .back-title { left: 140px; top: 24px; width: 270px; font-size: 50px; }
  .back-title .accent { font-size: 58px; }
  .blurb { left: 45px; top: 202px; width: 477px; font-family: "Tinos", serif; font-size: 13.3px; line-height: 16.5px; text-align: justify; color: var(--chalk); }
  .bio-photo { left: 43px; top: 452px; width: 96px; height: 130px; background: var(--paper); }
  .bio { left: 147px; top: 450px; width: 375px; font-family: "Tinos", serif; font-size: 13.3px; line-height: 16.5px; text-align: justify; }
  .bio-name { font-family: "Londrina Solid", sans-serif; font-weight: 900; color: var(--yellow); font-size: 19px; line-height: 22px; margin-bottom: 2px; }
  .code-box { top: 629px; width: 107px; height: 68px; background: var(--paper); }

  /* spine */
  .spine { left: 562px; top: 0; width: 90px; height: 727px; border-left: 1px solid #3f3f42; border-right: 1px solid #3f3f42; }
  .spine-text { position: absolute; left: 50%; transform: translateX(-50%); writing-mode: vertical-rl; font-family: "Londrina Solid", sans-serif; font-weight: 900; text-transform: uppercase; white-space: nowrap; }
  .spine-title { top: 30px; font-size: 31px; color: var(--chalk); }
  .spine-title .accent { color: var(--yellow); }
  .spine-author { top: 538px; font-size: 26px; color: var(--chalk); }

  /* front cover */
  .front-author { left: 700px; top: 16px; width: 440px; text-align: center; font-family: "Londrina Solid", sans-serif; font-weight: 900; font-size: 48px; color: var(--yellow); text-transform: uppercase; letter-spacing: 1px; }
  .chalk-word { position: absolute; font-family: "Cabin Sketch", sans-serif; font-weight: 700; color: var(--chalk-dim); white-space: nowrap; }
  .front-title { left: 690px; top: 218px; width: 480px; font-size: 92px; }
  .front-title .accent { font-size: 80px; line-height: 1.05; }
  .chalk-lines { position: absolute; left: 0; top: 0; }
</style>
</head>
<body>
<main class="cover">

  <!-- Back cover -->
  <section class="back-cover">
    <div class="sketch-art" style="left:64px;top:38px;width:70px;height:115px;" role="img" aria-label="Chalk sketch of a light bulb"></div>
    <div class="sketch-art" style="left:408px;top:52px;width:94px;height:92px;" role="img" aria-label="Chalk sketch of a brain"></div>
    <h2 class="abs title back-title">Venture<br>Keeper's<br><span class="accent">LanternBook</span></h2>

    <p class="abs blurb">Lorem ipsum dolor sit amet, consectetur adipiscing elit. Curabitur eget nibh blandit, consectetur justo a, suscipit augue. Mauris tellus turpis, sodales vel diam a, maximus malesuada odio. Integer luctus leo a convallis ullamcorper. Sed suscipit mauris ac tristique convallis. Ut vel elit porta, vehicula tellus ac, ornare neque. Integer pulvinar, sem sed efficitur facilisis, arcu sem sollicitudin enim, a tristique diam ex at libero. Cras euismod, enim non bibendum pretium, mi arcu sagittis quam, non luctus orci sem non orci. Praesent ullamcorper luctus pharetra. Vestibulum a mollis risus, nec bibendum ante. Suspendisse arcu odio, placerat consequat augue id, consectetur consequat risus. Suspendisse dapibus faucibus pharetra. Quisque cursus eros ipsum, vitae dapibus neque rhoncus in. Aenean ut mi bibendum nisl tempus vestibulum quis a dui.<br>disse arcu odio, placerat consequat augue id, consectetur consequat risus. Suspendisse dapibus faucibus pharetra. Quisque cursus eros ipsum, vitae dapibus neque rhoncus in. Aenean ut mi bibendum nisl tempus vestibulum quis a dui.</p>

    <div class="abs bio-photo"></div>
    <div class="abs bio">
      <div class="bio-name">CAL FERRAND</div>
      <p>Lorem ipsum dolor sit amet, consectetur adipiscing elit. Curabitur eget nibh blandit, consectetur justo a, suscipit augue. Mauris tellus turpis, sodales vel diam a, maximus malesuada odio. Integer luctus leo a convallis ullamcorper. Sed suscipit mauris ac tristique convallis. Ut vel elit porta, vehicula tellus ac, ornare neque. Integer pulvinar, sem sed efficitur facilisis, arcu sem sollicitudin enim, a tristique diam ex at libero.</p>
    </div>
    <div class="abs code-box" style="left:43px;"></div>
    <div class="abs code-box" style="left:415px;"></div>
  </section>

  <!-- Spine -->
  <section class="abs spine">
    <div class="spine-text spine-title">Venture Keeper's <span class="accent">LanternBook</span></div>
    <div class="spine-text spine-author">Cal Ferrand</div>
  </section>

  <!-- Front cover -->
  <section class="front-cover">
    <div class="abs front-author">Cal Ferrand</div>

    <span class="chalk-word" style="left:706px;top:80px;font-size:25px;color:var(--mint);">Goals</span>
    <span class="chalk-word" style="left:885px;top:88px;font-size:25px;">Analysis</span>
    <span class="chalk-word" style="left:1032px;top:104px;font-size:29px;">Marketing</span>
    <span class="chalk-word" style="left:672px;top:145px;font-size:25px;">Work Strategy</span>

    <div class="sketch-art" style="left:880px;top:128px;width:92px;height:84px;" role="img" aria-label="Chalk sketch of a brain"></div>
    <div class="sketch-art" style="left:662px;top:194px;width:72px;height:116px;" role="img" aria-label="Chalk sketch of a light bulb"></div>

    <svg class="chalk-lines" width="1200" height="727" viewBox="0 0 1200 727" aria-hidden="true">
      <g fill="none" stroke="#e6e6e6" stroke-width="2.2" stroke-linecap="round">
        <path d="M888 222 C870 160 840 118 782 102"/>
        <path d="M782 102 l12 -4 M782 102 l8 10"/>
        <path d="M878 222 C865 200 850 186 838 178"/>
        <path d="M838 178 l12 1 M838 178 l2 12"/>
        <path d="M1038 214 C1034 190 1042 168 1066 152"/>
        <path d="M1066 152 l-12 1 M1066 152 l-3 11"/>
        <path d="M904 478 C918 500 940 508 974 506"/>
        <path d="M974 506 l-9 -8 M974 506 l-9 8"/>
      </g>
      <g stroke="#2e2e30" stroke-width="1">
        <rect x="700" y="616" width="22" height="84" fill="#7fa45a"/>
        <rect x="740" y="644" width="22" height="56" fill="#a8534a"/>
        <rect x="780" y="650" width="22" height="50" fill="#b45a4c"/>
        <rect x="820" y="626" width="22" height="74" fill="#9fbf5a"/>
        <rect x="860" y="646" width="22" height="54" fill="#d8713f"/>
        <rect x="900" y="650" width="22" height="50" fill="#c2564a"/>
        <rect x="940" y="626" width="22" height="74" fill="#9cc35c"/>
        <rect x="980" y="616" width="22" height="84" fill="#a9c95a"/>
        <rect x="1020" y="616" width="22" height="84" fill="#86b85e"/>
        <rect x="1060" y="590" width="22" height="110" fill="#55bfa6"/>
        <rect x="1100" y="543" width="22" height="157" fill="#3f9ad6"/>
      </g>
      <g fill="#e0e0e0" opacity="0.35">
        <polygon points="700,616 706,610 728,610 722,616"/>
        <polygon points="1100,543 1106,537 1128,537 1122,543"/>
      </g>
    </svg>

    <h1 class="abs title front-title">Venture<br>Keeper's<br><span class="accent">LanternBook</span></h1>

    <span class="chalk-word" style="left:680px;top:500px;font-size:37px;">Timeline</span>
    <span class="chalk-word" style="left:1016px;top:488px;font-size:35px;">Success</span>
    <span class="chalk-word" style="left:870px;top:528px;font-size:42px;">Mission</span>
    <span class="chalk-word" style="left:735px;top:572px;font-size:21px;">Market</span>
  </section>

</main>
</body>
</html>
```